Business Card for Restaurant Business

I represent many restaurants from tiny clam shacks to extraordinary fine dining establishments. I need a business card. I was thinking maybe one that looked like a menu, but I'm open to suggestions. We are in a charming New England resort area (Cape Cod), so something coastal/nautical, but sophisticated.

```html
<!DOCTYPE html>
<html lang="en">
<head>
<meta charset="utf-8">
<title>Harbor Point Eateries — Business Card</title>
<link rel="stylesheet" href="https://fonts.googleapis.com/css2?family=Open+Sans:wght@400;600;700&family=Roboto+Slab:wght@600&display=swap">
<style>
  :root {
    --page-bg: #e6e8eb;
    --card-white: #ffffff;
    --brand-sky: #1b9ad6;
    --brand-deep: #1f5f8a;
    --brand-logo: #2b6f98;
    --ink: #333a40;
    --sky-top: #86bfe0;
    --sky-low: #c5dfee;
    --dune: #d8c9a4;
    --sea: #2f7fae;
    --sea-deep: #1e5f8a;
  }
  * { box-sizing: border-box; margin: 0; padding: 0; }
  html, body { width: 1200px; height: 964px; overflow: hidden; }
  body { background: var(--page-bg); position: relative; font-family: "Open Sans", Arial, sans-serif; }

  .card {
    position: absolute; left: 276px; width: 648px; height: 374px;
    border-radius: 20px; overflow: hidden;
    box-shadow: 0 3px 10px rgba(0,0,0,0.18);
  }

  /* Front */
  .card--front { top: 93px; }
  .front__photo {
    position: absolute; inset: 0;
    background: linear-gradient(180deg, var(--sky-top) 0%, var(--sky-low) 50%, var(--dune) 63%, #b9a57c 70%, var(--sea) 72%, var(--sea-deep) 100%);
  }
  .front__brand {
    position: absolute; left: 64px; top: 34px;
    display: flex; align-items: center; gap: 34px;
  }
  .brand-dot { width: 112px; height: 104px; border-radius: 50%; background: #fff; flex: none; }
  .brand-name {
    font-family: "Roboto Slab", Georgia, serif; font-weight: 600;
    color: #fff; font-size: 58px; line-height: 1.0; letter-spacing: 0.5px;
  }
  .front__social {
    position: absolute; left: 0; right: 0; top: 300px;
    display: flex; justify-content: center; align-items: center; gap: 6px;
  }
  .social-rule { width: 66px; height: 3px; background: #fff; margin: 0 12px; }
  .social-dot { width: 32px; height: 32px; border-radius: 50%; background: #fff; }

  /* Back */
  .card--back { top: 500px; background: var(--card-white); }
  .back__brand {
    position: absolute; right: 24px; top: 20px;
    display: flex; align-items: center; gap: 24px;
  }
  .back__brand .brand-dot { width: 84px; height: 76px; background: var(--brand-logo); }
  .back__brand .brand-name { color: var(--brand-logo); font-size: 45px; }

  .back__accent { position: absolute; left: 0; top: 164px; width: 8px; height: 39px; background: var(--brand-sky); }
  .person { position: absolute; left: 23px; top: 162px; }
  .person__name { font-size: 22px; font-weight: 700; color: var(--brand-deep); letter-spacing: 0.3px; line-height: 1.2; }
  .person__name span { color: var(--brand-sky); }
  .person__role { font-size: 17px; color: var(--ink); line-height: 1.3; }
  .back__rule { position: absolute; left: 23px; right: 23px; top: 219px; height: 2px; background: var(--brand-sky); }

  .contacts { position: absolute; left: 23px; top: 247px; list-style: none; }
  .contacts li { display: flex; align-items: center; gap: 6px; font-size: 17px; color: var(--ink); line-height: 21.5px; }
  .contacts svg { width: 14px; height: 14px; fill: var(--brand-sky); flex: none; }
  .address { position: absolute; right: 24px; top: 264px; text-align: right; font-size: 17px; color: var(--ink); line-height: 21px; font-style: normal; }

  .back__footer-line { position: absolute; left: 0; right: 0; bottom: 0; height: 8px; background: var(--brand-sky); }
  .back__footer-tab {
    position: absolute; right: 0; bottom: 0; width: 310px; height: 30px;
    background: var(--brand-deep);
    clip-path: polygon(12px 0, 100% 0, 100% 100%, 0 100%);
    color: #fff; font-size: 17px; display: flex; align-items: center; justify-content: flex-end; padding-right: 22px;
  }
</style>
</head>
<body>
  <section class="card card--front">
    <div class="front__photo" role="img" aria-label="Photograph of seaside cottages on a sandy shore with small boats on the water under a blue sky"></div>
    <div class="front__brand">
      <div class="brand-dot"></div>
      <div class="brand-name">Harbor Point<br>Eateries</div>
    </div>
    <div class="front__social">
      <div class="social-rule"></div>
      <div class="social-dot"></div>
      <div class="social-dot"></div>
      <div class="social-dot"></div>
      <div class="social-dot"></div>
      <div class="social-dot"></div>
      <div class="social-rule"></div>
    </div>
  </section>

  <section class="card card--back">
    <div class="back__brand">
      <div class="brand-dot"></div>
      <div class="brand-name">Harbor Point<br>Eateries</div>
    </div>

    <div class="back__accent"></div>
    <div class="person">
      <div class="person__name"><span>DANIEL</span> WHITFORD</div>
      <div class="person__role">Director</div>
    </div>
    <div class="back__rule"></div>

    <ul class="contacts">
      <li><svg viewBox="0 0 14 14"><path d="M4 0h6a1 1 0 0 1 1 1v12a1 1 0 0 1-1 1H4a1 1 0 0 1-1-1V1a1 1 0 0 1 1-1zm0.5 1.5v10h5v-10z"/></svg>508.555.0142</li>
      <li><svg viewBox="0 0 14 14"><path d="M3 1l2.5 0 1 3-1.5 1.2a8 8 0 0 0 3.8 3.8L10 7.5l3 1V11a1.5 1.5 0 0 1-1.5 1.5A10.5 10.5 0 0 1 1.5 2.5 1.5 1.5 0 0 1 3 1z"/></svg>508.555.0177</li>
      <li><svg viewBox="0 0 14 14"><path d="M3 1h8v3H3zM1 5h12v6h-2v2H3v-2H1zm3 4v3h6V9z"/></svg>508.555.0190</li>
      <li><svg viewBox="0 0 14 14"><path d="M1 3h12v8H1zm1 1v.4l5 3.3 5-3.3V4z"/></svg>hello@harborpointeats.com</li>
    </ul>

    <address class="address">27 Wharf Lane<br>P.O. Box 4410<br>Saltmarsh, MA 02630</address>

    <div class="back__footer-line"></div>
    <div class="back__footer-tab">www.harborpointeats.com</div>
  </section>
</body>
</html>
```